Website Design For Atelier Nine Design Group

Create a sophisticated website that denotes high-end luxury. We would like to keep the copy minimalist and elegantly understated while communicating only the most essential information. While creating an air of exclusivity.
We would like 3-4 Tab Wesbite
Home:
• Feature a design project front and centre, along with a short
introduction about who we are and what we do.

We can put a Call To Action at the end of the introduction inviting readers to learn more on our About page.
About:
• This page should provide more detail on our background, past
achievements, history of the company, and anything you'd like to
highlight.
• We should also provide details on our services, aesthetic, process, etc.
Team:
• introduce the team, possibly with short descriptions for each
team member. Total Team Members 7
Residential
• The portfolio page can be a grid of images along with titles for
each project.
• Clicking on each image should take you to a separate page for that
project where readers can find more details

Commercial
The portfolio page can be a grid of images along with titles for
each project.

Contact Us:

example website:
https://www.venkorahinteriors.example/

Target Market(s)

High end luxury clientele

Industry/Entity Type

Interior Design

Number of Pages Required

4 page

Font styles to use
Sans Serif

Requirements
Must have
• Company logo, color scheme and name: Atelier Nine Design Group

```html
<!DOCTYPE html>
<html lang="en">
<head>
<meta charset="utf-8">
<title>Atelier Nine Design Group</title>
<link rel="stylesheet" href="https://fonts.googleapis.com/css2?family=Barlow:wght@400;500;700&family=Barlow+Condensed:wght@600;700&family=Montserrat:wght@400;500;600&display=swap">
<style>
:root{
  --navy:#0a3344;
  --teal:#1d4a5a;
  --deep:#053546;
  --gold:#c9a045;
  --gold-soft:#e0b552;
  --ink:#1d2a30;
  --paper:#ffffff;
  --mist:#e6e8ea;
  --frame-grey:#cfcfcf;
}
*{margin:0;padding:0;box-sizing:border-box}
html,body{width:1200px;height:2804px;overflow:hidden;background:var(--paper)}
body{position:relative;font-family:"Barlow",sans-serif;color:var(--ink)}
.abs{position:absolute}

/* header */
.brand{position:absolute;left:0;width:1200px;text-align:center;color:var(--navy);font-family:"Barlow Condensed",sans-serif;font-weight:700;line-height:1}
.brand .mark{display:inline-block;width:30px;height:30px;background:var(--gold);margin-bottom:14px}
.brand .name{display:block;letter-spacing:6px}
.brand .sub{display:block;letter-spacing:7px;margin-top:8px}
.brand-top{top:28px}
.brand-top .name{font-size:62px}
.brand-top .sub{font-size:18px}

.nav{position:absolute;top:215px;left:0;width:1200px;height:55px;background:var(--gold);font-family:"Montserrat",sans-serif;font-size:20px;color:var(--paper)}
.nav a{position:absolute;top:0;height:55px;line-height:55px;color:inherit;text-decoration:none}
.nav .active{background:var(--paper);color:var(--navy);left:144px;width:110px;text-align:center}

/* hero */
.hero{position:absolute;top:270px;left:0;width:1200px;height:554px;background:linear-gradient(100deg,#163f4e 0%,#1f5162 55%,#1a4656 100%)}
.hero-welcome{left:98px;top:110px;font-family:"Montserrat",sans-serif;font-size:33px;color:var(--paper)}
.hero-rule{left:304px;top:128px;width:216px;height:2px;background:var(--paper)}
.hero-title{left:96px;top:142px;font-family:"Barlow Condensed",sans-serif;font-weight:700;color:var(--paper);font-size:138px;line-height:1;letter-spacing:-1px}
.hero-title .g{color:var(--gold)}
.hero-sub{left:96px;top:280px;font-family:"Barlow Condensed",sans-serif;font-weight:700;color:var(--gold);font-size:94px;line-height:1}
.btn{position:absolute;height:55px;border:2px solid var(--gold);font-family:"Montserrat",sans-serif;font-weight:600;font-size:18px;text-align:center;line-height:51px}
.hero .btn{color:var(--paper);top:398px;width:159px}
.hero-frame{left:578px;top:38px;width:482px;height:482px;border:52px solid var(--paper)}
.hero-photo{left:632px;top:92px;width:372px;height:374px;border:11px solid var(--teal);background:linear-gradient(135deg,#b9b9b9,#e9e9ea 55%,#9a9590)}

/* who we are */
.who-kicker{top:893px;left:0;width:1200px;text-align:center;font-family:"Montserrat",sans-serif;font-size:27px;color:var(--navy)}
.who-title{top:938px;left:0;width:1200px;text-align:center;font-weight:700;font-size:44px;color:var(--navy);letter-spacing:1px}
.who-title .g{color:var(--gold)}
.who-text{top:1016px;left:202px;width:797px;font-size:19.5px;line-height:31.3px;text-align:justify;text-align-last:center;letter-spacing:.3px}
.watermark{top:1255px;left:0;width:1200px;text-align:center;font-family:"Montserrat",sans-serif;font-weight:600;font-size:128px;color:var(--mist);letter-spacing:-4px;line-height:1.1}

/* featured */
.featured{position:absolute;top:1386px;left:0;width:1200px;height:448px;background:var(--paper)}
.feat-panel{left:0;top:0;width:452px;height:448px;background:var(--deep);overflow:hidden}
.feat-vert{left:-150px;top:190px;transform:rotate(-90deg);font-family:"Montserrat",sans-serif;font-weight:600;font-size:76px;color:rgba(255,255,255,.12);letter-spacing:1px;width:380px;text-align:center}
.feat-title{left:96px;top:66px;font-weight:700;font-size:44px;line-height:53px;color:var(--gold);letter-spacing:1px}
.feat-text{left:97px;top:190px;width:285px;font-size:15.5px;line-height:19.5px;color:var(--paper);text-align:justify}
.arrow{position:absolute;top:341px;width:53px;height:48px}
.arrow.prev{left:99px;background:#e4e4e4}
.arrow.next{left:164px;background:var(--gold)}
.arrow svg{position:absolute;left:17px;top:14px}
.tile{position:absolute;top:0;height:448px}
.tile-a{left:452px;width:320px;background:linear-gradient(160deg,#d9ad46,#e8bf58 60%,#cfa444)}
.tile-b{left:777px;width:320px;background:linear-gradient(160deg,#3d5148,#c9c3b8 50%,#9b948a)}
.tile-c{left:1102px;width:98px;background:linear-gradient(160deg,#3b5046,#d8d3c9 55%,#8a7a6a)}
.plus{left:576px;top:186px;width:77px;height:75px;background:var(--paper)}

/* what we do */
.wwd-frame{left:70px;top:1907px;width:218px;height:213px;border:9px solid var(--frame-grey)}
.wwd-photo{left:98px;top:1938px;width:397px;height:408px;background:linear-gradient(160deg,#3c5048,#d2ccc2 45%,#a39c92)}
.wwd-inset{left:380px;top:2174px;width:220px;height:216px;border:9px solid var(--gold);background:linear-gradient(135deg,#b8b8b8,#ececec 55%,#9a958f)}
.wwd-title{left:632px;top:1925px;font-weight:700;font-size:44px;color:var(--navy);letter-spacing:1px}
.wwd-rule{left:638px;top:1994px;width:464px;height:2px;background:var(--gold)}
.wwd-rule-bold{left:638px;top:1991px;width:70px;height:5px;background:var(--gold)}
.wwd-text{left:635px;top:2018px;width:467px;font-size:19px;line-height:24.8px;text-align:justify;letter-spacing:.3px}
.wwd-btn{left:635px;top:2290px;width:159px;color:var(--navy)}

/* footer */
.foot-rule{left:0;top:2455px;width:1200px;height:1px;background:#dcdcdc}
.brand-foot{top:2478px}
.brand-foot .name{font-size:56px}
.brand-foot .sub{font-size:16px}
.contact{top:2644px;left:0;width:1200px;text-align:center;font-size:18px;color:var(--ink)}
.contact b{color:var(--gold);font-weight:500}
.social{top:2688px;left:441px;width:320px;height:47px}
.social span{position:absolute;top:0;width:47px;height:47px;border-radius:50%;background:var(--gold)}
.copyright{left:0;top:2765px;width:1200px;height:39px;background:var(--gold);text-align:center;line-height:39px;font-size:14px;color:var(--paper)}
</style>
</head>
<body>

<header class="brand brand-top">
  <span class="mark"></span>
  <span class="name">ATELIER NINE</span>
  <span class="sub">DESIGN GROUP</span>
</header>

<nav class="nav">
  <a class="active">Home</a>
  <a style="left:291px">About Us</a>
  <a style="left:446px">Team</a>
  <a style="left:564px">Residential</a>
  <a style="left:737px">Commercial</a>
  <a style="left:923px">Contact Us</a>
</nav>

<section class="hero" role="img" aria-label="Dimmed photograph of a luxury bathroom with a freestanding tub">
  <div class="abs hero-welcome">Welcome to</div>
  <div class="abs hero-rule"></div>
  <div class="abs hero-title">ATELIER <span class="g">9</span></div>
  <div class="abs hero-sub">DESIGN GROUP</div>
  <div class="btn" style="left:98px">READ MORE</div>
  <div class="btn" style="left:272px">ABOUT US</div>
  <div class="abs hero-frame"></div>
  <div class="abs hero-photo" role="img" aria-label="Marble bathroom with white freestanding bathtub and stone side stool"></div>
</section>

<div class="abs who-kicker">Who We Are</div>
<h2 class="abs who-title"><span class="g">ATELIER NINE</span> DESIGN GROUP</h2>
<p class="abs who-text">Lorem Ipsum is simply dummy text of the printing and typesetting industry. Lorem Ipsum has been the industry's standard dummy text ever since the 1500s, when an unknown printer took a galley of type and scrambled it to make a type specimen book. It has survived not only five centuries, but also the leap into electronic typesetting, remaining essentially unchanged. It was popularised in the 1960s with the release of Letraset sheets containing Lorem Ipsum passages, and more recently with desktop publishing software like Aldus PageMaker including versions of Lorem Ipsum.</p>
<div class="abs watermark">WHO WE ARE</div>

<section class="featured">
  <div class="abs feat-panel">
    <div class="abs feat-vert">FEATURED</div>
    <h3 class="abs feat-title">FEATURED<br>PROJECT</h3>
    <p class="abs feat-text">Lorem Ipsum is simply dummy text of the printing and typesetting industry. Lorem Ipsum has been the industry's standard dummy text ever since the 1500s, when an unknown printer took a galley of type and scrambled it.</p>
    <div class="arrow prev"><svg width="18" height="20" viewBox="0 0 18 20"><path d="M12 2 L5 10 L12 18" fill="none" stroke="#333" stroke-width="2.5"/></svg></div>
    <div class="arrow next"><svg width="18" height="20" viewBox="0 0 18 20"><path d="M6 2 L13 10 L6 18" fill="none" stroke="#fff" stroke-width="2.5"/></svg></div>
  </div>
  <div class="tile tile-a" role="img" aria-label="Bathroom project with freestanding tub under a gold overlay"></div>
  <div class="abs plus"><svg width="77" height="75" viewBox="0 0 77 75"><path d="M38.5 20 V55 M21 37.5 H56" stroke="#c9a045" stroke-width="2.5"/></svg></div>
  <div class="tile tile-b" role="img" aria-label="Living room with patterned drapes, sofa and coffee table"></div>
  <div class="tile tile-c" role="img" aria-label="Sitting area with upholstered chair and built-in shelving"></div>
</section>

<div class="abs wwd-frame"></div>
<div class="abs wwd-photo" role="img" aria-label="Living room with window seat, drapes and sofa"></div>
<div class="abs wwd-inset" role="img" aria-label="Bathroom with freestanding tub"></div>
<h2 class="abs wwd-title">WHAT WE DO</h2>
<div class="abs wwd-rule"></div>
<div class="abs wwd-rule-bold"></div>
<p class="abs wwd-text">Lorem Ipsum is simply dummy text of the printing and typesetting industry. Lorem Ipsum has been the industry's standard dummy text ever since the 1500s, when an unknown printer took a galley of type and scrambled it to make a type specimen book. It has survived not only five centuries, but also the leap into electronic typesetting, remaining essentially unchanged. It was popularised in the 1960s with the release of Letraset sheets containing Lorem Ipsum passages, and more recently with desktop.</p>
<div class="btn wwd-btn">READ MORE</div>

<footer>
  <div class="abs foot-rule"></div>
  <div class="brand brand-foot">
    <span class="mark"></span>
    <span class="name">ATELIER NINE</span>
    <span class="sub">DESIGN GROUP</span>
  </div>
  <div class="abs contact"><b>Address:</b> Harbor Point, TX 77000, USA &nbsp;|&nbsp; <b>Phone:</b> 5550142876 &nbsp;|&nbsp; <b>Email:</b> hello@ateliernine.example</div>
  <div class="abs social" aria-label="Social links">
    <span style="left:0"></span>
    <span style="left:66px"></span>
    <span style="left:131px"></span>
    <span style="left:203px"></span>
    <span style="left:270px"></span>
  </div>
  <div class="abs copyright">Copyright © Atelier Nine Design Group | All Rights Reserved 2022</div>
</footer>

</body>
</html>
```